Rural photograpy business card design

I need a business card for my photography business, brianna delys photography. I would like my logo and pre designed font used on the card. Also my business specialises in photographing rural australia (e.g. shearing sheds, livestock, landscapes, farms), so a rural or country feel to the card would be great. I would like to keep the colours fresh but not too overpowering or juvenile.
Updates

Hi,

Could you please add my facebook page to the card - www.snapfolio-example.com/Brianna/Delys/Photography.
Thanks,
Brianna.

Reason: I have uploaded two photos I would like either one used on the card.

Target Market(s)

Farmers, country people from their mid twenties onwards

Industry/Entity Type

Business

Contact Information for Business Card

Brianna Delys Photography. Brianna Pemberton. 5182 Yarrowby-Tullagong Road, Tullagong Qld 4517. 0471602394.

Requirements
Must have
• My pre-designed logo and font. Also please add my facebook address - www.snapfolio-example.com/BriannaDelys/Photography.
Please use one of the photos I have provided.
Should not have
• Peoples faces on the card.

```html
<!DOCTYPE html>
<html lang="en">
<head>
<meta charset="utf-8">
<title>Brianna Delys Photography – Business Card</title>
<link rel="stylesheet" href="https://fonts.googleapis.com/css2?family=Questrial&display=swap">
<style>
  :root {
    --page-bg: #ffffff;
    --sky-deep: #3f5c9c;
    --sky-mid: #7f97d0;
    --sky-pale: #c3cbe6;
    --sun-glow: #f7c35a;
    --dust-amber: #b8731e;
    --ground-dark: #2a1a0c;
    --ground-deep: #140c05;
    --brand-ink: #1b1b1f;
    --text-light: #ffffff;
    --text-shadow: rgba(0, 0, 0, 0.85);
    --social-square: #3b5998;
  }

  html, body {
    margin: 0;
    padding: 0;
    width: 1200px;
    height: 1000px;
    overflow: hidden;
    background: var(--page-bg);
    font-family: "Questrial", "Century Gothic", sans-serif;
  }

  .business-card {
    position: absolute;
    left: 75px;
    top: 200px;
    width: 1051px;
    height: 600px;
    overflow: hidden;
  }

  .landscape-photo {
    position: absolute;
    inset: 0;
    background:
      radial-gradient(ellipse 340px 220px at 24% 66%, rgba(255, 214, 120, 0.95), rgba(247, 195, 90, 0.35) 55%, rgba(247, 195, 90, 0) 100%),
      linear-gradient(180deg,
        var(--sky-deep) 0%,
        var(--sky-mid) 30%,
        var(--sky-pale) 58%,
        var(--dust-amber) 72%,
        var(--ground-dark) 82%,
        var(--ground-deep) 100%);
  }

  .brand-name {
    position: absolute;
    left: 560px;
    top: 186px;
    width: 480px;
    text-align: center;
    color: var(--brand-ink);
    font-weight: 400;
    line-height: 1.2;
  }
  .brand-name .brand-primary {
    display: block;
    font-size: 44px;
    letter-spacing: 3px;
  }
  .brand-name .brand-secondary {
    display: block;
    font-size: 36px;
    letter-spacing: 2px;
  }

  .contact-text {
    position: absolute;
    color: var(--text-light);
    text-shadow: 0 0 2px var(--text-shadow), 1px 1px 2px var(--text-shadow);
    margin: 0;
  }

  .address {
    left: 38px;
    top: 490px;
    font-size: 27px;
    line-height: 41px;
    font-style: normal;
  }

  .contact-details {
    right: 40px;
    top: 442px;
    text-align: right;
  }
  .contact-details .person-name {
    display: block;
    font-size: 35px;
    line-height: 44px;
    margin-bottom: 4px;
  }
  .contact-details .contact-line {
    display: flex;
    justify-content: flex-end;
    align-items: center;
    gap: 12px;
    font-size: 26px;
    line-height: 40px;
  }
  .contact-line .icon {
    width: 30px;
    height: 30px;
    flex: none;
  }
  .social-square {
    width: 30px;
    height: 30px;
    background: var(--social-square);
    border-radius: 4px;
    flex: none;
  }
</style>
</head>
<body>
  <section class="business-card">
    <div class="landscape-photo" role="img" aria-label="Photograph of a rural Australian landscape at sunset: silhouetted gum trees against a blue sky, low sun glowing through golden dust over dark paddocks"></div>

    <div class="brand-name">
      <span class="brand-primary">BRIANNA DELYS</span>
      <span class="brand-secondary">PHOTOGRAPHY</span>
    </div>

    <address class="contact-text address">
      5182 Yarrowby-Tullagong Road<br>
      Tullagong Qld 4517
    </address>

    <div class="contact-text contact-details">
      <span class="person-name">Brianna Pemberton</span>
      <span class="contact-line">
        0471602394
        <svg class="icon" viewBox="0 0 24 24" aria-hidden="true">
          <path fill="#ffffff" d="M6.6 2.5c.5-.3 1.1-.2 1.4.3l2.2 3.6c.3.5.2 1.1-.2 1.4L8.6 9c.9 2.4 2.5 4.7 4.6 6.3l1.4-1.3c.4-.4 1-.4 1.4-.1l3.4 2.4c.5.3.6 1 .3 1.4l-1.4 2.1c-.5.8-1.5 1.1-2.4.8C9.6 18.6 5 13.3 3.9 7.1c-.2-.9.2-1.8 1-2.3z"/>
        </svg>
      </span>
      <span class="contact-line">
        BriannaDelysPhotography
        <span class="social-square" aria-hidden="true"></span>
      </span>
    </div>
  </section>
</body>
</html>
```